CRIMSON LANTERN DAY$

We need a postcard to promote a referall program that we are offering to everyone that has purchased a vehicle from us in the past 3 years - - -about 500.
The promotion is titled "crimson Lantern Days" and offers the recipient to earn up to $600, to be passed out the week of Tgiving.

We would require 3 coupons per card 100, 200, 300,and our logo and artwork.
I want it to blast out, catch enough attentioin to read
Front artwork and coupons, back description and rules.

Target Market(s)

our car and truck buyers from the past three years.

Requirements
Must have
• The Front of the postcard should have our Logo, the Promotion and three coupons.
Referal #1 - $100
Referal #2 - $200
Refreal #3 - $300
Each should name the promotion and have a spot for the person refering to write their name.

The back will promote the sale,and provide the timing, and rules.
Nice to have
• fits the excitement of the Season

```html
<!DOCTYPE html>
<html lang="en">
<head>
<meta charset="utf-8">
<title>Crimson Lantern Days Postcard</title>
<link href="https://fonts.googleapis.com/css2?family=Oswald:wght@500;700&family=Roboto+Condensed:wght@400;700&display=swap" rel="stylesheet">
<style>
  :root{
    --navy:#15263f;
    --red:#e0262b;
    --white:#ffffff;
    --bg:#efeae3;
    --line:#9a9a9a;
  }
  *{margin:0;padding:0;box-sizing:border-box}
  html,body{width:735px;height:1200px;overflow:hidden;background:var(--bg)}
  .canvas{position:relative;width:735px;height:1200px}
  .card{position:absolute;background:var(--white);overflow:hidden;box-shadow:0 3px 10px rgba(0,0,0,.18)}
  .card svg.shapes{position:absolute;left:0;top:0}
  .card-front{left:37px;top:62px;width:670px;height:518px}
  .card-back{left:32px;top:638px;width:679px;height:525px}
  .txt{position:absolute;font-family:"Oswald",sans-serif;color:var(--navy);line-height:1;white-space:nowrap}
  .promo-title{left:28px;top:24px;font-size:25px;font-weight:700;font-style:italic;letter-spacing:.3px}
  .headline{left:38px;top:112px;font-size:46px;font-weight:700;letter-spacing:.5px}
  .amount{left:36px;top:166px;font-size:94px;font-weight:700;color:var(--red)}
  .handout{left:42px;top:268px;font-size:18px;font-weight:700;line-height:1.25;letter-spacing:.3px}
  .coupon-value{font-size:34px;font-weight:700;color:var(--red);width:124px;text-align:center}
  .coupon-line{font-family:"Roboto Condensed",sans-serif;font-size:22px;font-weight:700;color:var(--navy);width:124px;text-align:center;letter-spacing:3px}
  .coupon-label{font-family:"Roboto Condensed",sans-serif;font-size:16px;font-weight:700;color:var(--white);width:160px;text-align:center}
  .address{left:524px;top:436px;font-family:"Roboto Condensed",sans-serif;font-size:13px;font-weight:700;color:var(--white);line-height:1.35}
  .phone{left:524px;top:472px;font-size:19px;font-weight:700;color:var(--white)}
  .brand{display:flex;align-items:center;gap:6px;font-family:"Oswald",sans-serif;font-weight:700;font-size:15px;color:var(--navy);position:absolute;white-space:nowrap}
  .brand-mark{width:11px;height:11px;background:var(--red)}
  .back-title{left:28px;top:228px;font-size:28px;font-weight:700;letter-spacing:.3px}
  .offer{left:28px;top:266px;font-family:"Roboto Condensed",sans-serif;font-size:15px;line-height:1.12;letter-spacing:.2px}
  .timing{left:28px;top:326px;font-size:21px;font-weight:700;padding-bottom:4px;border-bottom:2px dashed var(--navy);width:138px}
  .rules{left:0;top:371px;width:110px;height:26px;background:var(--red);border-radius:0 13px 13px 0;color:var(--white);font-size:18px;font-weight:700;padding:2px 0 0 30px}
  .rule-list{left:30px;top:408px;list-style:none;font-family:"Roboto Condensed",sans-serif;font-size:15px;line-height:1.35}
  .rule-list li::before{content:"";display:inline-block;width:8px;height:8px;border-radius:50%;background:var(--red);margin-right:6px}
  .website{left:26px;top:486px;font-family:"Roboto Condensed",sans-serif;font-size:19px;font-weight:700;color:var(--white);letter-spacing:.3px}
</style>
</head>
<body>
<div class="canvas">

  <section class="card card-front">
    <svg class="shapes" width="670" height="518" viewBox="0 0 670 518">
      <defs>
        <linearGradient id="car-tone" x1="0" y1="0" x2="1" y2="1">
          <stop offset="0" stop-color="#b7a7a3"/>
          <stop offset=".55" stop-color="#3b56a8"/>
          <stop offset="1" stop-color="#6d6f73"/>
        </linearGradient>
        <linearGradient id="arrow-tone" x1="0" y1="0" x2="1" y2="0">
          <stop offset="0" stop-color="#d9d9d9"/>
          <stop offset="1" stop-color="#555"/>
        </linearGradient>
      </defs>
      <path d="M0,92 C100,74 220,74 305,98" fill="none" stroke="var(--navy)" stroke-width="8"/>
      <path d="M0,104 C100,86 220,86 305,110" fill="none" stroke="var(--red)" stroke-width="3"/>
      <path d="M322,0 C302,60 292,130 300,190 C315,262 372,302 452,297 C540,292 610,266 670,240 L670,0 Z" fill="var(--navy)"/>
      <path d="M338,0 C316,60 306,130 314,188 C328,256 382,291 452,287 C540,281 610,258 670,232 L670,0 Z" fill="var(--red)"/>
      <path d="M352,0 C328,60 320,130 327,185 C341,250 392,282 455,278 C540,272 610,250 670,224 L670,0 Z" fill="url(#car-tone)" role="img" aria-label="Photo of a blue sedan parked on a lot"/>
      <path d="M470,262 C540,250 590,230 618,208 L606,196 L660,205 L628,250 L622,232 C590,258 530,275 470,262 Z" fill="url(#arrow-tone)"/>
      <rect x="0" y="406" width="511" height="12" fill="var(--red)"/>
      <rect x="0" y="418" width="511" height="100" fill="var(--navy)"/>
      <rect x="511" y="406" width="159" height="112" fill="var(--red)"/>
      <g fill="var(--white)" stroke="var(--red)" stroke-width="6">
        <circle cx="93" cy="393" r="62"/>
        <circle cx="260" cy="393" r="62"/>
        <circle cx="425" cy="393" r="62"/>
      </g>
    </svg>

    <h1 class="txt promo-title">CRIMSON LANTERN DAYS</h1>
    <p class="txt headline">EARN UP TO</p>
    <p class="txt amount">$600</p>
    <p class="txt handout">TO BE PASSED OUT<br>THE WEEK OF TGIVING</p>

    <div class="txt coupon-value" style="left:31px;top:355px">$100</div>
    <div class="txt coupon-line" style="left:31px;top:400px">------</div>
    <div class="txt coupon-label" style="left:13px;top:478px">REFERAL #1</div>

    <div class="txt coupon-value" style="left:198px;top:355px">$200</div>
    <div class="txt coupon-line" style="left:198px;top:400px">------</div>
    <div class="txt coupon-label" style="left:180px;top:478px">REFERAL #2</div>

    <div class="txt coupon-value" style="left:363px;top:355px">$300</div>
    <div class="txt coupon-line" style="left:363px;top:400px">------</div>
    <div class="txt coupon-label" style="left:345px;top:478px">REFERAL #3</div>

    <div class="brand" style="left:530px;top:330px"><span class="brand-mark"></span>MERIDIAN MOTORS</div>

    <p class="txt address">4180 HARBOR RTE 9<br>LAKEVIEW, MI 49000</p>
    <p class="txt phone">555-018-4420</p>
  </section>

  <section class="card card-back">
    <svg class="shapes" width="679" height="525" viewBox="0 0 679 525">
      <defs>
        <linearGradient id="lot-tone" x1="0" y1="0" x2="0" y2="1">
          <stop offset="0" stop-color="#7f9a5e"/>
          <stop offset=".3" stop-color="#b9c0c6"/>
          <stop offset="1" stop-color="#5e6368"/>
        </linearGradient>
        <linearGradient id="arrow-tone-b" x1="0" y1="0" x2="1" y2="0">
          <stop offset="0" stop-color="#d9d9d9"/>
          <stop offset="1" stop-color="#555"/>
        </linearGradient>
      </defs>
      <path d="M0,0 L455,0 C450,120 420,190 300,205 C200,215 110,185 0,182 Z" fill="var(--navy)"/>
      <path d="M0,0 L440,0 C436,112 405,176 296,191 C200,202 110,174 0,170 Z" fill="var(--red)"/>
      <path d="M0,0 L428,0 C424,104 394,166 292,179 C200,190 110,162 0,158 Z" fill="url(#lot-tone)" role="img" aria-label="Photo of a row of cars for sale on a dealer lot"/>
      <path d="M250,190 C320,180 370,150 395,115 L382,104 L438,100 L418,150 L408,132 C380,170 320,200 250,190 Z" fill="url(#arrow-tone-b)"/>
      <path d="M455,0 C462,140 430,210 380,300 C345,365 340,430 348,525" fill="none" stroke="var(--navy)" stroke-width="10"/>
      <path d="M0,467 L328,467 C332,485 336,505 340,525 L0,525 Z" fill="var(--red)"/>
      <rect x="556" y="40" width="84" height="85" fill="none" stroke="#8c8c8c" stroke-width="1.5"/>
      <g stroke="var(--line)" stroke-width="1.5">
        <line x1="383" y1="240" x2="636" y2="240"/>
        <line x1="383" y1="287" x2="636" y2="287"/>
        <line x1="383" y1="334" x2="636" y2="334"/>
        <line x1="383" y1="382" x2="636" y2="382"/>
      </g>
    </svg>

    <h2 class="txt back-title">CRIMSON LANTERN DAYS</h2>
    <p class="txt offer">WE ARE OFFERING TO EVERYONE THAT<br>HAS PURCHASED A VEHICLE FROM US IN<br>THE PAST 3 YEARS - - -ABOUT 500</p>
    <h3 class="txt timing">SALES TIMING</h3>
    <h3 class="txt rules">RULES</h3>
    <ul class="txt rule-list">
      <li>LOREM IPSUM DOLOR SIT AMET</li>
      <li>LOREM IPSUM DOLOR SIT AMET</li>
    </ul>
    <p class="txt website">WWW.MERIDIANMOTORS.EXAMPLE</p>

    <div class="brand" style="left:520px;top:462px"><span class="brand-mark"></span>MERIDIAN MOTORS</div>
  </section>

</div>
</body>
</html>
```